Classic Minimalistic Business Card

Design a classic, minimalistic Business Card. Please find inspiration in the attached Classic Minimalistic examples. My information:
Name: Glen Ovamir
Company: Ovamir Capital
Logo: OC
Address: 1470 N Thornwick Rd, Suite 210 | Larkfield, ST 00000
Phone: 555-555-0192
Email: glenovamir@pvt.insure
Slogan: Building Strength Through Capital

Feel free to leave out any of the information above except my name.

I have selected Double-sided, but I am also open to Single-sided

Target Market(s)

22-70. income greater than 150k/year

Industry/Entity Type

Finance

Contact Information for Business Card

See Project Description

Requirements
Must have
• Ivory or "antiqued" background similar to the reference pictures

```html
<!DOCTYPE html>
<html lang="en">
<head>
<meta charset="utf-8">
<title>Ovamir Capital – Business Card</title>
<link rel="stylesheet" href="https://fonts.googleapis.com/css2?family=Poppins:ital,wght@0,300;0,400;0,600;1,300&display=swap">
<style>
  :root {
    --stage: #2a2f36;
    --ivory: #f1e7d6;
    --ivory-mid: #e6d6bc;
    --aged-edge: #b8946a;
    --ink: #1d1b1a;
    --ink-soft: #3b3633;
    --brand-red: #e51f26;
    --brand-blush: rgba(236, 128, 100, 0.62);
  }
  * { box-sizing: border-box; margin: 0; padding: 0; }
  html, body { width: 1200px; height: 780px; overflow: hidden; }
  body {
    background: var(--stage);
    font-family: "Poppins", sans-serif;
    display: flex;
    align-items: center;
    justify-content: center;
    gap: 48px;
  }
  .card {
    position: relative;
    width: 525px;
    height: 300px;
    border-radius: 18px;
    overflow: hidden;
    background:
      radial-gradient(ellipse at 50% 45%, var(--ivory) 0%, var(--ivory) 45%, var(--ivory-mid) 78%, var(--aged-edge) 118%);
    box-shadow: 0 18px 40px rgba(0, 0, 0, 0.45);
    color: var(--ink);
  }

  /* Front */
  .card--front {
    display: flex;
    align-items: center;
    justify-content: center;
  }
  .brand {
    display: flex;
    flex-direction: column;
    align-items: flex-start;
    position: relative;
    padding-top: 78px;
  }
  .brand__square {
    position: absolute;
    top: 0;
    right: 18px;
    width: 84px;
    height: 84px;
    background: var(--brand-red);
  }
  .brand__name {
    font-weight: 600;
    font-size: 44px;
    line-height: 1.1;
    letter-spacing: -0.5px;
    color: var(--ink);
    margin-top: 14px;
  }
  .brand__tagline {
    font-weight: 300;
    font-size: 17px;
    color: var(--ink-soft);
    margin-top: 2px;
    letter-spacing: 0.2px;
  }

  /* Back */
  .card--back { padding: 36px 0 0 38px; }
  .back__decor {
    position: absolute;
    right: -30px;
    bottom: -40px;
    width: 230px;
    height: 230px;
    background: var(--brand-blush);
  }
  .person__name {
    position: relative;
    font-weight: 600;
    font-size: 27px;
    line-height: 1.1;
  }
  .person__title {
    position: relative;
    font-weight: 300;
    font-style: italic;
    font-size: 14px;
    color: var(--ink-soft);
    margin-top: 2px;
  }
  .contact {
    position: relative;
    list-style: none;
    margin-top: 18px;
    font-weight: 300;
    font-size: 15px;
    line-height: 1.45;
    color: var(--ink);
  }
  .contact__item { display: flex; align-items: flex-start; gap: 8px; }
  .contact__icon { width: 13px; height: 13px; margin-top: 5px; flex: none; fill: var(--ink); }
</style>
</head>
<body>

  <section class="card card--front" aria-label="Card front">
    <div class="brand">
      <span class="brand__square" aria-hidden="true"></span>
      <h1 class="brand__name">Ovamir Capital</h1>
      <p class="brand__tagline">Building Strength Through Capital</p>
    </div>
  </section>

  <section class="card card--back" aria-label="Card back">
    <span class="back__decor" aria-hidden="true"></span>
    <h2 class="person__name">Glen Ovamir</h2>
    <p class="person__title">Director of Operations</p>
    <ul class="contact">
      <li class="contact__item">
        <svg class="contact__icon" viewBox="0 0 16 16" aria-hidden="true"><rect x="0" y="2" width="16" height="12" rx="1.5"/><path d="M1.5 3.5 8 9l6.5-5.5" stroke="#f1e7d6" stroke-width="1.6" fill="none"/></svg>
        <span>glenovamir@pvt.insure</span>
      </li>
      <li class="contact__item">
        <svg class="contact__icon" viewBox="0 0 16 16" aria-hidden="true"><path d="M4 1c1 0 1.8 2.6 1.8 3.4 0 .9-1.4 1.3-1.3 2 .4 1.7 2.4 3.7 4.1 4.1.7.1 1.1-1.3 2-1.3.8 0 3.4.8 3.4 1.8 0 1.6-1.6 3-3 3C5.6 14 2 10.4 2 4.9 2 2.6 3 1 4 1z"/></svg>
        <span>555-555-0192</span>
      </li>
      <li class="contact__item">
        <svg class="contact__icon" viewBox="0 0 16 16" aria-hidden="true"><path d="M8 0a5.5 5.5 0 0 0-5.5 5.5C2.5 10 8 16 8 16s5.5-6 5.5-10.5A5.5 5.5 0 0 0 8 0zm0 7.7a2.2 2.2 0 1 1 0-4.4 2.2 2.2 0 0 1 0 4.4z"/></svg>
        <span>1470 N Thornwick Rd,<br>Suite 210 | Larkfield, ST 00000</span>
      </li>
    </ul>
  </section>

</body>
</html>
```